Website Design Front page Holistic Members site & Natural Therapist Directory

I need a modern, fresh unique look for a natural therapy and holistic/ Spiritual directory & educational website. It needs to be clear, colourful, inviting and suitable for both sexes - young and old. I want it look fresh and super modern.

I will require the design in .psd format and anything in the centre section including rotational image needs to be supplied in .ai so I can break down the components and colours used will also be needed for frames and banners.

Target Market(s)

all ages, male and female. It must appeal to both therapists and general public.

Requirements
Must have
• Logo obviously. Room for a video player 300 x 250. And small introduction text panel. Must follow the layout in file attached. Also a rotating image up the top, in main section (have supplied example image alter as you like - man pointing top right). Have also supplied example of text to have on it. 16 Menu bars on left frame, under home. Must have 6 prominent links to main pages of site. Have included images use if you want or else use your own. These 6 are, Find a Psychic/ Medium, Find a Natural Therapist, Find a Business/ Club/ School, Find an Event/ Workshop, Find a Product, Holistic Career Centre.I have also attached a shot of the emag, although nothing special in design, useful for complimentary colour choices but not limited to. Another link image/ banner would be Free Chat Now.Another if room and not over crowded would be compare memberships. Can use leader board and leader ad board. Also require the footer to be designed and delivered in .ai similar to lantern vale with link image to Velunari and Trevasso.
Nice to have
• Compare memberships link would be great but not essential... don't want page to look too busy.
Should not have
• Must not be too busy.. think zen with a modern twist.

```html
<!DOCTYPE html>
<html lang="en">
<head>
<meta charset="utf-8">
<title>Soul Chorus – Community &amp; Chat Rooms</title>
<link href="https://fonts.googleapis.com/css2?family=Arimo:wght@400;700&display=swap" rel="stylesheet">
<style>
:root{
  --blue:#1566b7;
  --blue-dark:#0f4f98;
  --blue-light:#2f86d6;
  --orange:#f08a0c;
  --orange-light:#f7a634;
  --orange-line:#fbc16b;
  --green:#7fc92f;
  --green-light:#a6e05a;
  --text:#333;
  --link:#1a6cc0;
  --panel:#f1f1f1;
  --border:#d4d4d4;
  --white:#fff;
}
*{box-sizing:border-box;margin:0;padding:0}
html,body{width:870px;height:1200px;overflow:hidden}
body{font-family:"Arimo",Arial,sans-serif;color:var(--text);background:var(--white);position:relative;font-size:10px}
a{text-decoration:none;color:inherit}

/* header */
.site-header{position:absolute;left:0;top:0;width:870px;height:115px;background:linear-gradient(#fff,#eef1f4)}
.brand{position:absolute;left:40px;top:36px;display:flex;align-items:center;gap:8px}
.brand-dot{width:34px;height:34px;border-radius:50%;background:var(--orange)}
.brand-name{font-size:26px;font-weight:700;color:#222;letter-spacing:-.5px}
.util-tab{position:absolute;left:631px;top:0;width:191px;height:34px;background:linear-gradient(#f4f4f4,#dcdcdc);border-radius:0 0 6px 6px;box-shadow:0 2px 4px rgba(0,0,0,.25);display:flex;justify-content:center;align-items:center;gap:6px;font-size:11.5px;color:#444}
.util-tab .sep{color:#888}

/* main nav */
.main-nav{position:absolute;left:0;top:115px;width:870px;height:34px;background:linear-gradient(var(--blue-light),var(--blue));display:flex;align-items:center;padding-left:24px}
.main-nav a{color:#fff;font-size:12.2px;padding:4px 8px;margin-right:3px;white-space:nowrap}
.main-nav a.active{background:#fff;color:#222;border-radius:2px}

/* left column */
.community-search{position:absolute;left:0;top:149px;width:174px;height:76px}
.community-search h2{font-weight:400;font-size:14px;color:#444;position:absolute;left:12px;top:10px}
.search-field{position:absolute;left:12px;top:33px;width:150px;height:25px;border:1px solid var(--border);border-radius:3px;background:#fff;font-size:10px;color:#555;padding:6px 5px}
.search-field .btn{position:absolute;right:0;top:0;width:25px;height:23px;border-left:1px solid var(--border)}
.side-menu{position:absolute;left:0;top:225px;width:174px;list-style:none}
.side-menu li{height:24.7px;background:linear-gradient(var(--orange-light),var(--orange));border-bottom:1px solid var(--orange-line);color:#6b2e00;font-weight:700;font-size:10.8px;padding:6px 0 0 12px;position:relative;white-space:nowrap}
.side-menu li.current{color:#fff}
.side-menu li.more::after{content:"";position:absolute;right:10px;top:8px;border:4px solid transparent;border-left:5px solid #7a3a00}

.featured{position:absolute;left:3px;top:579px;width:171px;height:422px;background:var(--panel);border:1px solid var(--border);border-radius:4px;overflow:hidden}
.featured h3{height:33px;background:linear-gradient(var(--green-light),var(--green));color:#fff;font-weight:400;font-size:14px;padding:8px 10px}
.practitioner{position:relative;border-bottom:1px solid var(--border);padding:8px 0 0 9px}
.practitioner h4{font-size:11px;color:#333;margin-bottom:5px}
.practitioner .photo{position:absolute;left:10px;top:26px;width:52px;height:52px;background:linear-gradient(135deg,#c9a98a,#8a6a55)}
.practitioner p{margin-left:61px;padding-right:4px;font-size:9.6px;line-height:12px;color:#444}
.practitioner p b{display:block;font-size:8px;line-height:10px;color:#222}

/* hero */
.hero{position:absolute;left:174px;top:149px;width:520px;height:272px;background:linear-gradient(180deg,#1f74c4 0%,#4ea0e0 45%,#8ec9ee 62%,#dfe8ef 75%,#f2f2f0 100%)}
.hero-photo{position:absolute;left:14px;top:85px;width:110px;height:145px;border-radius:40px 40px 8px 8px;background:linear-gradient(#d8c2ad,#f5f5f5)}
.hero h1{position:absolute;left:140px;top:46px;font-size:28px;font-weight:700;color:#fff;letter-spacing:.6px;white-space:nowrap;text-shadow:0 2px 3px rgba(0,0,0,.25)}
.join-btn{position:absolute;left:247px;top:134px;width:172px;height:44px;background:linear-gradient(#fff,#e4e4e4);border-radius:4px;box-shadow:0 2px 4px rgba(0,0,0,.3);font-size:19px;color:#555;text-align:center;line-height:44px}

/* sign in */
.signin{position:absolute;left:694px;top:149px;width:176px;height:272px;background:linear-gradient(var(--blue-light),var(--blue));color:#fff;padding:9px 10px}
.signin h2{font-size:14px;font-weight:700;margin-bottom:12px}
.signin label{display:block;font-size:10.5px;margin-bottom:3px}
.signin .input{height:27px;background:#fff;border-radius:3px;margin-bottom:15px;width:153px}
.signin .remember{display:flex;align-items:center;gap:5px;font-size:10px}
.signin .remember span{width:11px;height:11px;background:#fff}
.signin-btn{position:absolute;left:78px;top:189px;width:82px;height:27px;background:linear-gradient(var(--orange-light),var(--orange));border-radius:4px;font-size:11.5px;line-height:27px;padding-left:12px}
.signin-btn svg{position:absolute;right:7px;top:6px}
.signin .links{position:absolute;right:12px;top:228px;text-align:right;font-size:9px;line-height:13.5px}
.signin .links a{text-decoration:underline}

/* welcome */
.welcome{position:absolute;left:206px;top:461px;width:184px}
.welcome h2{font-size:13px;font-weight:400;line-height:18px;color:#333;margin-bottom:16px;white-space:nowrap;letter-spacing:-.2px}
.welcome h2 span{color:var(--link)}
.welcome p{font-size:9.4px;line-height:12.3px;color:#333}
.welcome .tag{color:var(--link);margin-top:13px;font-size:10px}

.video{position:absolute;left:406px;top:462px;width:255px;height:216px;background:#111}
.video-screen{position:absolute;left:0;top:0;width:255px;height:185px;background:linear-gradient(#1a2c6e,#3c6ec4 45%,#9bc7ea 55%,#2a4d98 80%,#0b1b48)}
.video-title{position:absolute;left:9px;top:6px;color:#fff;font-size:9px}
.play{position:absolute;left:104px;top:80px;width:46px;height:30px;background:rgba(0,0,0,.75);border-radius:5px}
.video-bar{position:absolute;left:0;top:192px;width:255px;height:24px;background:linear-gradient(#f6f6f6,#d5d5d5);display:flex;align-items:center;font-size:8.5px;color:#333}
.video-bar .cell{height:24px;border-right:1px solid #bbb;display:flex;align-items:center;justify-content:center}

.divider{position:absolute;left:190px;top:722px;width:490px;height:8px;background:radial-gradient(ellipse at top,rgba(0,0,0,.14),transparent 70%)}

/* finder links */
.finder{position:absolute;width:138px}
.finder h3{font-size:12px;font-weight:400;color:var(--link);white-space:nowrap;letter-spacing:-.4px;margin-bottom:4px}
.finder .thumb{width:138px;height:86px;border:1px solid #ddd;box-shadow:0 1px 3px rgba(0,0,0,.2)}

/* right column */
.calendar{position:absolute;left:694px;top:431px;width:172px;height:320px;border:1px solid var(--border);border-radius:4px;background:var(--panel);overflow:hidden}
.calendar h2{height:34px;background:linear-gradient(var(--orange-light),var(--orange));color:#fff;font-weight:400;font-size:14px;padding:9px 11px}
.event{border-bottom:1px solid var(--border);padding:7px 12px 6px;font-size:9.6px;line-height:12.2px;color:#444}
.event b{display:block;color:#333}
.promo{position:absolute;left:694px;width:172px;height:44px;border-radius:4px;color:#fff;font-weight:700;box-shadow:0 1px 3px rgba(0,0,0,.3)}
.promo.chat{top:760px;background:linear-gradient(var(--green-light),var(--green));font-size:20px;padding:11px 20px}
.promo.search{top:814px;background:linear-gradient(var(--orange-light),var(--orange));font-size:16px;line-height:17px;padding:5px 20px}
.promo.edu{top:869px;background:linear-gradient(var(--blue-light),var(--blue-dark));font-size:16px;line-height:17px;padding:5px 20px}
.promo svg{position:absolute;right:12px;top:8px}
.magazine{position:absolute;left:694px;top:924px;width:172px;height:96px;border:1px solid var(--border);border-radius:4px;background:#fff}
.magazine h3{font-size:13px;color:var(--blue);text-align:center;margin-top:6px}
.magazine .covers{position:absolute;left:24px;top:25px;width:125px;height:64px;background:linear-gradient(120deg,#f3c27a,#f7f1e6,#e8a24a)}

/* footer */
.site-footer{position:absolute;left:0;top:1062px;width:870px;height:138px;background:var(--blue-dark);border-top:4px solid #8ec0ea;color:#fff}
.site-footer h4{position:absolute;left:26px;top:13px;font-size:11px}
.foot-links{position:absolute;top:38px;list-style:none;font-size:10.5px;line-height:15.3px}
.copyright{position:absolute;right:26px;top:13px;font-size:10.5px}
.social{position:absolute;right:28px;width:84px;height:30px;border-radius:4px;display:flex;align-items:center;justify-content:center;font-size:14px;font-weight:700;color:#fff}
.social.velunari{top:40px;background:#3b5ea8}
.social.trevasso{top:81px;background:#3fa9e0}
</style>
</head>
<body>

<header class="site-header">
  <div class="brand"><span class="brand-dot"></span><span class="brand-name">soul chorus</span></div>
  <nav class="util-tab"><span>contact us</span><span class="sep">|</span><span>sign in</span><span class="sep">|</span><span>register</span></nav>
</header>

<nav class="main-nav">
  <a class="active">Home</a><a>Career Centre</a><a>Education Centre</a><a>Therapist Finder</a><a>Psychic Finder</a><a>Business Finder</a><a>Events Calendar</a><a>Social Community</a>
</nav>

<aside>
  <section class="community-search">
    <h2>Community Search</h2>
    <div class="search-field">enter search criteria
      <span class="btn"><svg width="24" height="23"><circle cx="11" cy="10" r="5" fill="none" stroke="#777" stroke-width="1.5"/><line x1="15" y1="14" x2="19" y2="18" stroke="#777" stroke-width="2"/></svg></span>
    </div>
  </section>
  <ul class="side-menu">
    <li class="current">Home</li><li class="more">Memberships</li><li>Search Practitioner Directory</li><li>View Business Members</li><li class="more">Free Chat Rooms</li><li>Online Store</li><li>Events Calendar</li><li class="more">Glossary</li><li>Career Center</li><li class="more">Featured Profiles</li><li class="more">Monthly Updates</li><li class="more">Advertise With Us</li><li>FAQ</li><li>Site Search</li>
  </ul>
  <section class="featured">
    <h3>Featured Practitioners</h3>
    <div class="practitioner" style="height:91px"><h4>Seer Mira</h4><div class="photo" role="img" aria-label="Portrait of practitioner"></div><p>Psychic/Medium, Reiki Master, Trance Channeler, Author, Workshop Facilitator.<b>Stillwater Circle</b></p></div>
    <div class="practitioner" style="height:90px"><h4>Rhea Linwood</h4><div class="photo" role="img" aria-label="Portrait of practitioner"></div><p>Tarot, Numerologist, Reiki Master, Crystal Therapist, Author, Workshop Facilitator.<b>Moonpath Tarot</b></p></div>
    <div class="practitioner" style="height:91px"><h4>Tessa Maybrook-Hale</h4><div class="photo" role="img" aria-label="Portrait of practitioner"></div><p>Reconnective Healer, NLP Master.</p></div>
    <div class="practitioner" style="height:120px;border:0"><h4>Odette Fairlow</h4><div class="photo" role="img" aria-label="Portrait of practitioner"></div><p>Spiritual Artist, Flower Essence Practitioner, Workshop Facilitator.<b>Halcyon Art Gallery &amp; Healing Centre</b></p></div>
  </section>
</aside>

<section class="hero">
  <div class="hero-photo" role="img" aria-label="Man meditating on the beach, pointing to the top right"></div>
  <h1>SHARE. LEARN. GROW</h1>
  <div class="join-btn">Join Now</div>
</section>

<section class="signin">
  <h2>Sign In</h2>
  <label>Username</label><div class="input"></div>
  <label>Password</label><div class="input"></div>
  <div class="remember"><span></span>Remember Me</div>
  <div class="signin-btn">Sign In<svg width="16" height="16"><circle cx="8" cy="8" r="7" fill="none" stroke="#fff" stroke-width="1.2"/><path d="M6.5 5l3.5 3-3.5 3z" fill="#fff"/></svg></div>
  <div class="links"><a>Forgot Password?</a><br><a>Haven't Registered Yet?</a></div>
</section>

<main>
  <section class="welcome">
    <h2>WELCOME TO <span>SOUL CHORUS<br>COMMUNITY &amp; CHAT ROOMS</span></h2>
    <p>We hope you will explore the various features our site has to offer. We created this online space for log on and create a dynamic member profile, collaborate on projects, share your ideas and expertise - and, most important, connect with your fellow members. Share, collaborate, exchange and grow - that's why we're here and we hope you are too. Engage and explore anytime, from anywhere there's a web connection.</p>
    <p class="tag">Share. Learn. Grow.</p>
  </section>

  <section class="video">
    <div class="video-screen" role="img" aria-label="Video still of a tree reflected in still water at dusk"></div>
    <span class="video-title">Om Shanti</span>
    <svg class="play" viewBox="0 0 46 30"><path d="M18 8l12 7-12 7z" fill="#fff"/></svg>
    <div class="video-bar">
      <div class="cell" style="width:26px"><svg width="10" height="10"><path d="M1 0l9 5-9 5z" fill="#333"/></svg></div>
      <div class="cell" style="width:28px"><svg width="14" height="10"><path d="M0 3h3l4-3v10l-4-3H0z" fill="#333"/><path d="M9 2q3 3 0 6" fill="none" stroke="#333"/></svg></div>
      <div class="cell" style="width:130px;justify-content:flex-start;padding-left:8px">0:00 / 6:26</div>
      <div class="cell" style="width:44px;font-weight:700">Ovrelin</div>
      <div class="cell" style="width:27px;border:0"><svg width="11" height="11" fill="none" stroke="#333"><path d="M0 4V0h4M7 0h4v4M11 7v4H7M4 11H0V7"/></svg></div>
    </div>
  </section>

  <div class="divider"></div>

  <a class="finder" style="left:206px;top:752px"><h3>FIND A PSYCHIC</h3><div class="thumb" role="img" aria-label="Candle, old book and tarot cards" style="background:linear-gradient(#2a1a10,#7a5230 55%,#e8e0d0)"></div></a>
  <a class="finder" style="left:366px;top:752px"><h3>FIND A THERAPIST</h3><div class="thumb" role="img" aria-label="Head massage treatment" style="background:linear-gradient(#e9eef6,#f4d8c6 60%,#eaeaea)"></div></a>
  <a class="finder" style="left:524px;top:752px"><h3>FIND A BUSINESS/SCHOOL</h3><div class="thumb" role="img" aria-label="Warmly lit treatment room" style="background:linear-gradient(#a88a3a,#6a4a20 55%,#b07040)"></div></a>
  <a class="finder" style="left:206px;top:891px"><h3>FIND AND EVENT</h3><div class="thumb" role="img" aria-label="Hand writing in a planner" style="background:linear-gradient(135deg,#f4f4f4,#d8dde6)"></div></a>
  <a class="finder" style="left:366px;top:891px"><h3>FIND A PRODUCT</h3><div class="thumb" role="img" aria-label="Essential oil bottles and flowers" style="background:linear-gradient(135deg,#f3e6e6,#b88a5a 55%,#e7a0c0)"></div></a>
  <a class="finder" style="left:524px;top:891px"><h3>HOLISTIC CAREER CENTRE</h3><div class="thumb" role="img" aria-label="Jobs sign against the sky" style="background:linear-gradient(135deg,#9ec8ee,#2e5ea8 60%,#1a3d7a)"></div></a>
</main>

<aside>
  <section class="calendar">
    <h2>Calendar</h2>
    <div class="event"><b>2/02/2011</b>Stillwater Circle - Monthly Meditation Circle</div>
    <div class="event"><b>19/02/2011 - 5/04/2011</b>Stillwater Circle - General Psychic Development Workshop - 2 Days</div>
    <div class="event"><b>26/02/2011 - 27/02/2011</b>Stillwater Circle - Deep Meditation Workshop Master Meditation</div>
    <div class="event"><b>6/03/2011</b>Stillwater Circle - The Art of Manifesting Workshop</div>
    <div class="event" style="border:0"><b>19/03/2011 - 20/03/2011</b>Stillwater Circle - Angel Card Reading Workshop</div>
  </section>
  <div class="promo chat">Free Chat<svg width="42" height="28" fill="#fff" stroke="#aaa"><ellipse cx="16" cy="11" rx="14" ry="9"/><ellipse cx="28" cy="16" rx="12" ry="8"/></svg></div>
  <div class="promo search">Search<br>Directory<svg width="32" height="30"><circle cx="13" cy="12" r="9" fill="rgba(255,255,255,.3)" stroke="#ddd" stroke-width="2"/><line x1="20" y1="19" x2="29" y2="28" stroke="#666" stroke-width="4"/></svg></div>
  <div class="promo edu">Education<br>Centre<svg width="22" height="30"><circle cx="11" cy="11" r="9" fill="#e6f79a"/><rect x="7" y="20" width="8" height="7" fill="#ccc"/></svg></div>
  <section class="magazine"><h3>Monthly Online Magazine</h3><div class="covers" role="img" aria-label="Fanned magazine covers"></div></section>
</aside>

<footer class="site-footer">
  <h4>Site Map</h4>
  <ul class="foot-links" style="left:26px"><li>Career Centre</li><li>Education Centre</li><li>Therapist Finder</li><li>Psychic Finder</li></ul>
  <ul class="foot-links" style="left:133px"><li>Business Finder</li><li>Events Calendar</li><li>Social Community</li></ul>
  <p class="copyright">Copyright © 2011 Soulchorus</p>
  <a class="social velunari">velunari</a>
  <a class="social trevasso">trevasso</a>
</footer>

</body>
</html>
```